Business Card Needed for Crafter of Pottery, Jewelry and Artwork

Calling all designers in search of an artistic challenge.

I need a new business card design for my pottery, jewelry and artwork business, Woven Glass and Tide, based in Vancouver BC.

I would like a card that is bright and inviting and preferably incorporates my logo and a sample of photos of my work while having a clean fresh look. The following contact details would preferably be included on the card as well:
• Helena Pikeworth
• Designer
• Phone: 604.555.0172
• Email: Designer@WovenGlassandTide.example
• Website: www.WovenGlassandTide.example
• Blog: www.ShapingHillside.example

The logo is attached in two color schemes in both Vector and Source formats. On past cards I’ve also included photos of my work. By including photos of the work the pieces are showcased and it catches people’s eye and prompts them to pick up the card and look at it more closely. For example, if I leave a stack in a coffee shop I want people to be drawn to the card, to pick it up and get a sense of the my product lines. Please feel free to pull photos of my work directly off of my website. If you need photos with higher pixels please let me know and I’ll email them directly to you. The website background is bffbda (191, 251, 218). I would like the business cards to match the feel of the website for consistency but the cards do not need to use the exact same colors. My website and current business card are predominantly turquoise shades. The background uses stripes provided by the website template. I don’t know the exact colors of the stripes.

My current business card is attached to show the use of photos in a design. Please note that I am not thrilled with my own design and am looking for variations and completely new designs. This example is not meant to be used as a template or starting point.

Here is some background surrounding my company:
WGT offers one of a kind jewelry, pottery, artwork and leather bags each designed with a twist. The pottery varies from rustic every day functional ware to raku artwork. The jewelry ranges from simple sterling every day pieces to multimedia pieces incorporating stone, metal, ceramics and fabric. The artwork is multimedia, typically acrylic paired with a natural element such as bark. All the bags are leather with reworked kimono fabric or patterned silk lining.

Feel free to check out my website to get a flavour for my work and the color scheme I've used on marketing materials so far. www.wovenglassandtide.example
Updates

Thank you to everyone who has submitted a design so far. I hope everyone has received some helpful feedback.

I'm going to post a survey to customers and friends asking for their votes. If you have new designs to submit please try to get them in by Saturday March 30 at noon so that I can include it in the survey launch.

Thank you

Target Market(s)

Females aged 25-65 interested in one of a kind functional pottery and jewelry.

Industry/Entity Type

Coffee Shop

Requirements
Must have
• Contact information, website, blog
Nice to have
• Logo, photos

```html
<!DOCTYPE html>
<html lang="en">
<head>
<meta charset="utf-8">
<title>Woven Glass and Tide – Business Card</title>
<link rel="stylesheet" href="https://fonts.googleapis.com/css2?family=Libre+Baskerville:wght@400;700&family=Tinos&display=swap">
<style>
  :root {
    --teal: #16958f;
    --teal-deep: #0f7f7a;
    --paper: #ffffff;
    --cream: #fbf7d2;
    --stage: #e8e8e4;
    --ink-light: #ffffff;
  }
  * { margin: 0; padding: 0; box-sizing: border-box; }
  html, body { width: 1200px; height: 741px; overflow: hidden; }
  body { background: var(--stage); position: relative; font-family: "Tinos", "Times New Roman", serif; }

  .card {
    position: absolute;
    left: 245px;
    width: 673px;
    height: 304px;
    background: var(--paper);
    overflow: hidden;
    box-shadow: 0 2px 8px rgba(0,0,0,0.12);
  }
  .card--front { top: 30px; }
  .card--back { top: 392px; }

  /* Front */
  .contact-band {
    position: absolute;
    left: 64px; top: 0;
    width: 229px; height: 304px;
    background: var(--teal);
    color: var(--ink-light);
  }
  .person-name {
    position: absolute;
    right: 14px; top: 31px;
    font-family: "Libre Baskerville", Georgia, serif;
    font-weight: 700;
    font-size: 19px;
    white-space: nowrap;
  }
  .person-role {
    position: absolute;
    right: 14px; top: 56px;
    font-size: 13px;
  }
  .contact-list {
    position: absolute;
    left: 9px; top: 190px;
    list-style: none;
    font-size: 11.5px;
    line-height: 15.6px;
    white-space: nowrap;
  }
  .brand-name {
    position: absolute;
    left: 300px; top: 70px;
    width: 300px; height: 164px;
    display: flex; flex-direction: column;
    align-items: center; justify-content: center;
    font-family: "Libre Baskerville", Georgia, serif;
    font-weight: 400;
    color: var(--teal);
    text-align: center;
    font-size: 30px;
    line-height: 1.2;
    letter-spacing: 1px;
  }

  /* Back */
  .title-band, .url-band {
    position: absolute;
    left: 0; width: 673px;
    background: var(--teal);
    color: var(--ink-light);
    text-align: center;
    font-family: "Libre Baskerville", Georgia, serif;
  }
  .title-band { top: 39px; height: 34px; font-size: 24px; line-height: 34px; }
  .url-band { top: 230px; height: 36px; font-size: 23px; line-height: 36px; }
  .side-panel { position: absolute; top: 83px; height: 147px; background: var(--cream); }
  .side-panel--left { left: 0; width: 61px; }
  .side-panel--right { left: 650px; width: 23px; }
  .work-photo { position: absolute; top: 111px; height: 118px; }
  .work-photo--raku { left: 89px; width: 228px; background: linear-gradient(160deg, #e9e2dc 0%, #7a3a3e 40%, #4a5a78 65%, #c8a98a 100%); }
  .work-photo--vase { left: 317px; width: 115px; background: linear-gradient(180deg, #f0ede8 0%, #6b3d22 35%, #5f4a33 55%, #6fb89a 80%, #d9d2c4 100%); }
  .work-photo--mugs { left: 432px; width: 186px; background: linear-gradient(180deg, #f4f4f2 0%, #b9d6d3 40%, #8fb4b3 65%, #5a5d60 85%, #eeeeec 100%); }
</style>
</head>
<body>
  <section class="card card--front" aria-label="Card front">
    <div class="contact-band">
      <p class="person-name">Helena Pikeworth</p>
      <p class="person-role">Designer</p>
      <ul class="contact-list">
        <li>604.555.0172</li>
        <li>Designer@WovenGlassandTide.example</li>
        <li>www.WovenGlassandTide.example</li>
        <li>www.ShapingHillside.example</li>
      </ul>
    </div>
    <p class="brand-name"><span>Woven Glass</span><span>and Tide</span></p>
  </section>

  <section class="card card--back" aria-label="Card back">
    <p class="title-band">Woven Glass and Tide</p>
    <div class="side-panel side-panel--left"></div>
    <div class="side-panel side-panel--right"></div>
    <div class="work-photo work-photo--raku" role="img" aria-label="Photo of raku pottery pieces with iridescent glazes"></div>
    <div class="work-photo work-photo--vase" role="img" aria-label="Photo of a brown and green glazed vase"></div>
    <div class="work-photo work-photo--mugs" role="img" aria-label="Photo of pale turquoise glazed mugs and pitcher"></div>
    <p class="url-band">www.WovenGlassandTide.example</p>
  </section>
</body>
</html>
```